Business Card Design Needed

Business car design required, logo will be supplied.

Brackenfield Heat Surveyors are looking to become the leading provider of energy performance certificates to estate agents, landlords and home owners in the Yorkshire region of the UK.

The business card must be double sided and professional looking. Estate agents receive hundreds of cards from contractors and our card must stand out.

I require a two sided business card that is clean, modern and created by a designer that can think outside of the box.

Brand colours can be supplied .

Please ask if you have any questions.

Target Market(s)

Estate agents, landlords and property owners

Industry/Entity Type

Property - estate agency - energy consultants

Contact Information for Business Card

Tomas Birchwell - Energy Assessor - 07351642170 - www.BrackenfieldHSV.co.uk - info@brackenfieldhsv.co.uk

Font styles to use
Serif
Sans Serif

Colors
00AB8E
00BBA5
67D7C9
C6EFE9
E9F9F6

Requirements
Must have
• Use the provided logo, clean, professional and stand out from the crowd
Nice to have
• Clever use of text, spacing and brand colours
Should not have
• Clip art

```html
<!DOCTYPE html>
<html lang="en">
<head>
<meta charset="utf-8">
<title>Brackenfield Heat Surveyors – Business Card</title>
<link rel="stylesheet" href="https://fonts.googleapis.com/css2?family=Open+Sans:wght@300;400;600&display=swap">
<style>
  :root {
    --brand-blue: #0a67a8;
    --brand-green: #b3d236;
    --ink: #2a2a2a;
    --paper: #ffffff;
    --backdrop: #e4e5e7;
    --card-shadow: 0 10px 28px rgba(0,0,0,0.22);
  }
  * { box-sizing: border-box; margin: 0; padding: 0; }
  html, body { width: 1200px; height: 804px; overflow: hidden; }
  body {
    background: var(--backdrop);
    font-family: "Open Sans", Arial, sans-serif;
    position: relative;
  }
  .card {
    position: absolute;
    top: 230px;
    width: 540px;
    height: 344px;
    background: var(--paper);
    box-shadow: var(--card-shadow);
    overflow: hidden;
  }
  .card--front { left: 40px; }
  .card--back { left: 620px; }

  /* brand lockup */
  .brand {
    position: absolute;
    display: flex;
    align-items: center;
  }
  .brand__dot {
    width: 62px; height: 62px;
    border-radius: 50%;
    background: var(--brand-blue);
    flex: none;
  }
  .brand__divider {
    width: 1.5px; height: 78px;
    background: var(--brand-blue);
    margin: 0 22px;
    flex: none;
  }
  .brand__name {
    color: var(--brand-blue);
    font-weight: 300;
    text-transform: uppercase;
    line-height: 1.15;
  }
  .brand__name-main { display: block; font-size: 40px; letter-spacing: 1px; }
  .brand__name-sub { display: block; font-size: 15px; letter-spacing: 8px; }

  .card--front .brand { left: 34px; top: 88px; }

  .web-band {
    position: absolute;
    left: 0; right: 0; bottom: 0;
    height: 62px;
    background: var(--brand-blue);
    color: var(--paper);
    font-size: 20px;
    font-weight: 400;
    display: flex;
    align-items: center;
    padding-left: 34px;
    letter-spacing: 0.3px;
  }

  /* back */
  .card--back .brand { left: 30px; top: 26px; }
  .card--back .brand__dot { width: 52px; height: 52px; }
  .card--back .brand__divider { height: 64px; margin: 0 18px; }
  .card--back .brand__name-main { font-size: 34px; }
  .card--back .brand__name-sub { font-size: 13px; letter-spacing: 7px; }

  .rule {
    position: absolute;
    left: 34px; right: 30px;
    top: 178px;
    height: 1.5px;
    background: var(--brand-blue);
  }
  .person {
    position: absolute;
    right: 34px;
    top: 144px;
    text-align: right;
  }
  .person__name {
    font-size: 25px;
    font-weight: 400;
    color: var(--ink);
    letter-spacing: 1.5px;
    line-height: 34px;
  }
  .person__role {
    font-size: 11px;
    color: var(--brand-green);
    letter-spacing: 1.5px;
    margin-top: 2px;
  }
  .contacts {
    position: absolute;
    left: 34px;
    bottom: 28px;
    list-style: none;
    font-size: 13px;
    color: var(--ink);
  }
  .contacts li {
    display: flex;
    align-items: center;
    gap: 10px;
    height: 21px;
  }
  .contacts svg { width: 14px; height: 14px; flex: none; }
  .address {
    position: absolute;
    right: 34px;
    bottom: 30px;
    display: flex;
    align-items: center;
    gap: 8px;
    font-size: 13px;
    color: var(--ink);
  }
  .address svg { width: 13px; height: 16px; }
</style>
</head>
<body>

<section class="card card--front" aria-label="Card front">
  <div class="brand">
    <span class="brand__dot"></span>
    <span class="brand__divider"></span>
    <h1 class="brand__name">
      <span class="brand__name-main">Brackenfield</span>
      <span class="brand__name-sub">Heat Surveyors</span>
    </h1>
  </div>
  <div class="web-band">www.BrackenfieldHSV.co.uk</div>
</section>

<section class="card card--back" aria-label="Card back">
  <div class="brand">
    <span class="brand__dot"></span>
    <span class="brand__divider"></span>
    <p class="brand__name">
      <span class="brand__name-main">Brackenfield</span>
      <span class="brand__name-sub">Heat Surveyors</span>
    </p>
  </div>

  <div class="rule"></div>

  <div class="person">
    <p class="person__name">Tomas Birchwell</p>
    <p class="person__role">Energy Assessor</p>
  </div>

  <ul class="contacts">
    <li>
      <svg viewBox="0 0 14 14" aria-hidden="true"><rect x="3" y="1" width="8" height="12" rx="1.5" fill="none" stroke="var(--brand-green)" stroke-width="1.4"/></svg>
      07351642170
    </li>
    <li>
      <svg viewBox="0 0 14 14" aria-hidden="true"><rect x="1" y="3" width="12" height="8" fill="var(--brand-green)"/><path d="M1 3 L7 8 L13 3" fill="none" stroke="#fff" stroke-width="1.2"/></svg>
      info@brackenfieldhsv.co.uk
    </li>
    <li>
      <svg viewBox="0 0 14 14" aria-hidden="true"><circle cx="7" cy="7" r="6" fill="var(--brand-green)"/></svg>
      www.profilehub.net/yourname
    </li>
  </ul>

  <div class="address">
    Your address
    <svg viewBox="0 0 13 16" aria-hidden="true"><path d="M6.5 15 C6.5 15 1 9 1 6 A5.5 5.5 0 0 1 12 6 C12 9 6.5 15 6.5 15Z" fill="var(--brand-green)"/><circle cx="6.5" cy="6" r="2" fill="#fff"/></svg>
  </div>
</section>

</body>
</html>
```